Creative Business Card

Were looking for a new fresh and creative look to our Business card. Our company name is InkHollow. Be creative, Were attaching our logo and our base colors, but your free to do anything. Name, title, Phone

Industry/Entity Type

Business

```html
<!DOCTYPE html>
<html lang="en">
<head>
<meta charset="utf-8">
<title>InkHollow Business Card</title>
<link rel="stylesheet" href="https://fonts.googleapis.com/css2?family=Source+Sans+3:wght@400;600;700&display=swap">
<style>
  :root {
    --backdrop: #9a7652;
    --card-front: #ffffff;
    --card-back: #000000;
    --brand-green: #7cc142;
    --brand-blue: #1a78c2;
    --ink: #1b1b1b;
    --ink-soft: #333333;
    --paper-text: #ffffff;
  }
  * { box-sizing: border-box; margin: 0; padding: 0; }
  html, body {
    width: 1200px;
    height: 900px;
    overflow: hidden;
    background: var(--backdrop);
    font-family: "Source Sans 3", "Myriad Pro", sans-serif;
  }
  .stage { position: relative; width: 1200px; height: 900px; }
  .card {
    position: absolute;
    left: 318px;
    width: 532px;
    height: 302px;
    border-radius: 40px;
    overflow: hidden;
    text-align: center;
    box-shadow: 0 2px 10px rgba(0,0,0,0.25);
  }
  .card--front { top: 131px; background: var(--card-front); }
  .card--back { top: 466px; background: var(--card-back); }

  .wordmark {
    position: absolute;
    left: 0; right: 0;
    font-weight: 700;
    color: var(--brand-green);
    letter-spacing: 1px;
    line-height: 1;
  }
  .card--front .wordmark { top: 54px; font-size: 86px; }
  .card--back .wordmark { top: 112px; font-size: 66px; }

  .edge-tab {
    position: absolute;
    right: 0;
    width: 8px;
  }
  .edge-tab--blue { top: 84px; height: 68px; background: var(--brand-blue); }
  .edge-tab--green { top: 152px; height: 67px; background: var(--brand-green); }

  .holder {
    position: absolute;
    top: 198px; left: 0; right: 0;
    font-size: 21px;
    line-height: 26px;
    color: var(--ink);
  }
  .holder__name { font-weight: 700; }
  .address {
    position: absolute;
    top: 236px; left: 0; right: 0;
    font-size: 16px;
    line-height: 20px;
    color: var(--ink-soft);
    word-spacing: 1px;
  }
  .contacts {
    position: absolute;
    top: 260px; left: 0; right: 0;
    font-size: 15.5px;
    line-height: 20px;
    color: var(--ink-soft);
    display: flex;
    justify-content: center;
    gap: 20px;
  }
  .contacts__label { font-weight: 700; font-style: italic; }
  .contacts__label--green { color: var(--brand-green); }
  .contacts__label--blue { color: var(--brand-blue); }

  .web {
    position: absolute;
    top: 200px; left: 0; right: 0;
    font-size: 16px;
    color: var(--paper-text);
  }
</style>
</head>
<body>
<main class="stage">
  <section class="card card--front" aria-label="Business card front">
    <div class="wordmark">InkHollow</div>
    <span class="edge-tab edge-tab--blue"></span>
    <span class="edge-tab edge-tab--green"></span>
    <p class="holder"><span class="holder__name">Marcus Ellery</span> Senior Tech</p>
    <p class="address">2450 Harbor Boulevard&nbsp;&nbsp; Cedar Vale, California</p>
    <p class="contacts">
      <span><span class="contacts__label contacts__label--green">t:</span>1(555) 214 0000</span>
      <span><span class="contacts__label contacts__label--blue">m:</span>1(555) 214 0000</span>
      <span><span class="contacts__label contacts__label--green">e:</span>info@inkhollow.com</span>
    </p>
  </section>

  <section class="card card--back" aria-label="Business card back">
    <div class="wordmark">InkHollow</div>
    <p class="web">inkhollow.com</p>
  </section>
</main>
</body>
</html>
```